Require stationery design: letter head and update existing business card

clean, simple, minamilistic, los of negative space, black or white. casual, but passionate, informative and knowledgable , no fuss, don to earth.

logo newly created and supplied As AI files in breif. . TO CONFIRM THE FINAL LOGO IS THE VERSION WITH THE GRAPHIC / PICTURE INCLUDED. we now need to update our business card design, take old logo out and replace with new logo, raw business files supplied in brief.
For business card I need proofs with white, black and ligjt timber / rustic cookie.

Target Market(s)

women, house wives, business men, hospitality, higher socio economic, commercial residential, niche market.

Industry/Entity Type

Business

Number of Pages Required

3 page

Font styles to use
Sans Serif

Colors
ffffff
3277b5
0355a3
faa54b
f68e4e

Requirements
Must have
• proofs for business card design to be provided on white, black, timber / cardboard background. logo and business to be supplied in all usable formats and files.
• Letter head to be A4 against white background. Supplier in WORDDOC or send header and footer images as JPEG so I can insert into word template
• suitable quote, invoice, receipt template for emailed pdf's
Nice to have
• stylised touch. finesse. sophistication. we are competed in this kind of market.
• use the colour featured in the screen shot file of a random logo
Should not have
• clutter. be crowded. more than 2 fonts.

```html
<!DOCTYPE html>
<html lang="en">
<head>
<meta charset="utf-8">
<title>Timber &amp; Grain Co. — Letterhead</title>
<link rel="stylesheet" href="https://fonts.googleapis.com/css2?family=Open+Sans:wght@400;600&display=swap">
<style>
  :root {
    --backdrop: #d9d89e;
    --paper: #fdfdf8;
    --ink: #555555;
    --ink-strong: #3d3d3d;
    --olive-dark: #6d6945;
    --olive-mid: #8f8b5d;
    --stone: #b7baba;
    --rule: #c4c4bc;
  }
  * { box-sizing: border-box; margin: 0; padding: 0; }
  html, body { width: 1200px; height: 784px; overflow: hidden; }
  body {
    background: var(--backdrop);
    font-family: "Open Sans", sans-serif;
    color: var(--ink);
  }
  .letterhead {
    position: absolute;
    left: 338px; top: 22px;
    width: 524px; height: 740px;
    background: var(--paper);
    box-shadow: 0 2px 10px rgba(80, 80, 40, 0.25);
    overflow: hidden;
  }
  .corner-accent {
    position: absolute; width: 96px; height: 96px;
    background: linear-gradient(135deg, var(--olive-dark), var(--olive-mid) 60%, var(--stone));
  }
  .corner-accent--top-right { top: 0; right: 0; clip-path: polygon(0 0, 100% 0, 100% 100%); }
  .corner-accent--bottom-left { bottom: 0; left: 0; clip-path: polygon(0 0, 0 100%, 100% 100%); }

  .brand {
    position: absolute; left: 56px; top: 44px;
    display: flex; align-items: center; gap: 8px;
  }
  .brand__dot { width: 12px; height: 12px; border-radius: 50%; background: var(--olive-mid); }
  .brand__name {
    font-size: 14px; font-weight: 600; letter-spacing: 0.08em;
    color: var(--ink-strong); text-transform: uppercase;
  }

  .letter { position: absolute; left: 56px; top: 118px; width: 400px; }
  .letter__greeting { font-size: 12px; font-weight: 600; color: var(--ink-strong); margin-bottom: 16px; }
  .letter__body p {
    font-size: 8.6px; line-height: 1.5; font-weight: 600;
    text-indent: 20px; margin-bottom: 10px; text-align: justify;
  }
  .letter__signature {
    display: block; width: 70px; height: 46px; margin: 24px 0 0 10px;
    background: linear-gradient(135deg, #e9e9e2, #d6d6cf);
    border-radius: 4px;
  }

  .footer {
    position: absolute; left: 0; right: 0; bottom: 36px;
    text-align: center; font-size: 7.2px; color: var(--ink);
  }
  .footer__row { display: flex; align-items: center; justify-content: center; gap: 10px; }
  .footer__rule { width: 46px; height: 1px; background: var(--rule); }
  .footer__icons { display: flex; justify-content: center; gap: 5px; margin-bottom: 6px; }
  .footer__icons svg { width: 9px; height: 9px; }
  .footer__line + .footer__line { margin-top: 3px; }
</style>
</head>
<body>
  <article class="letterhead">
    <div class="corner-accent corner-accent--top-right" role="img" aria-label="Decorative olive and grey corner accent"></div>
    <div class="corner-accent corner-accent--bottom-left" role="img" aria-label="Decorative olive and grey corner accent"></div>

    <header class="brand">
      <span class="brand__dot"></span>
      <span class="brand__name">Timber &amp; Grain Co.</span>
    </header>

    <section class="letter">
      <p class="letter__greeting">Dear Mr. Solicitor,</p>
      <div class="letter__body">
        <p>Lorem ipsum dolor sit amet, consectetur adipiscing elit. Vestibulum nec nunc sollicitudin, dictum ligula vitae, accumsan felis. Donec at quam felis. Pellentesque feugiat condimentum adipiscing. Maecenas sit amet neque ligula. Suspendisse ut libero in justo ullamcorper porttitor et vel orci. In consequat nibh in lacinia facilisis. Interdum et malesuada fames ac ante ipsum primis in faucibus. Cras adipiscing turpis lacus, eu faucibus nibh laoreet vel. Etiam pellentesque, massa eu sodales interdum, mi nisi sagittis sem, sit amet feugiat turpis erat ac arcu. Proin at tincidunt nulla, sed feugiat massa. Maecenas suscipit purus nec orci rutrum, non auctor eros vulputate. Ut nec erat mollis, placerat risus venenatis, pharetra quam. Mauris hendrerit interdum ante, nec molestie ipsum faucibus eu.</p>
        <p>Nulla nec risus non quam mollis volutpat. Suspendisse sit amet dignissim purus. Sed fringilla ipsum eu ullamcorper posuere. In odio odio, tempor eu dictum a, pulvinar eu eros. Sed suscipit id risus a rhoncus. Mauris mollis dictum libero, vel lacinia sapien ullamcorper quis. Ut nec erat mollis, placerat risus venenatis, pharetra quam. Mauris hendrerit interdum ante, nec molestie ipsum faucibus eu. Etiam ultricies, sapien quis blandit ullamcorper, diam diam mollis urna, sed tempor diam nulla ut odio. Cras sollicitudin semper convallis. Sed suscipit id risus a rhoncus.</p>
      </div>
      <span class="letter__signature" role="img" aria-label="Handwritten signature of the sender"></span>
    </section>

    <footer class="footer">
      <div class="footer__icons" aria-hidden="true">
        <svg viewBox="0 0 10 10"><circle cx="5" cy="5" r="5" fill="var(--olive-mid)"/><path d="M5 2.2a1.8 1.8 0 0 1 1.8 1.8C6.8 5.4 5 7.6 5 7.6S3.2 5.4 3.2 4A1.8 1.8 0 0 1 5 2.2z" fill="#fff"/></svg>
        <svg viewBox="0 0 10 10"><circle cx="5" cy="5" r="5" fill="var(--olive-mid)"/><path d="M3.2 2.6l1.1.1.4 1.2-.6.5a4 4 0 0 0 1.6 1.6l.5-.6 1.2.4.1 1.1c-2.3.3-4.6-2-4.3-4.3z" fill="#fff"/></svg>
        <svg viewBox="0 0 10 10"><circle cx="5" cy="5" r="5" fill="var(--olive-mid)"/><rect x="2.6" y="3.4" width="4.8" height="3.4" fill="#fff"/><path d="M2.6 3.4L5 5.3l2.4-1.9" stroke="var(--olive-mid)" stroke-width=".6" fill="none"/></svg>
        <svg viewBox="0 0 10 10"><circle cx="5" cy="5" r="5" fill="var(--olive-mid)"/><circle cx="5" cy="5" r="2.4" fill="none" stroke="#fff" stroke-width=".7"/><path d="M2.6 5h4.8" stroke="#fff" stroke-width=".6"/></svg>
      </div>
      <div class="footer__row">
        <span class="footer__rule"></span>
        <div>
          <p class="footer__line">Suite 0, 000 Harbour Rd, Kelston NZ 0000 | (00) 0000 0000 | (00) 0000 0000</p>
          <p class="footer__line">info@timberandgrain.co.nz | www.timberandgrain.co.nz</p>
        </div>
        <span class="footer__rule"></span>
      </div>
    </footer>
  </article>
</body>
</html>
```